Poster

I need a poster for my business, www.coastaltablejourneysbay.example which some information about the most important activities (Sangria Tasting, Iberian Ham, Charcuteries & Sherry Wine Tasting, Sailboat Experiences and Picnic Experiences). A3 Format. Social media included (@coastaltablejourneyctj), contact information included.

```html
<!DOCTYPE html>
<html lang="en">
<head>
<meta charset="utf-8">
<title>Coastal Table Journeys Bay — Poster</title>
<link href="https://fonts.googleapis.com/css2?family=Bebas+Neue&display=swap" rel="stylesheet">
<style>
  :root {
    --orange: #f1a01b;
    --white: #ffffff;
    --ink: #4a4a4a;
    --sky: #b9c9d1;
    --sea: #6f8896;
    --deck: #7d6a5c;
    --wood: #8f6248;
    --cured: #7a3a30;
    --mist: #e9e2da;
    --shadow: rgba(45, 25, 8, 0.75);
  }
  * { margin: 0; padding: 0; box-sizing: border-box; }
  html, body { width: 849px; height: 1200px; overflow: hidden; background: var(--white); }
  .poster {
    position: relative;
    width: 849px;
    height: 1200px;
    overflow: hidden;
    background: var(--orange);
    font-family: "Bebas Neue", "Oswald", sans-serif;
  }
  .hero-photo {
    position: absolute;
    left: 0; top: 150px;
    width: 849px; height: 890px;
    background:
      radial-gradient(ellipse 140px 300px at 345px 300px, rgba(60,50,45,0.55), transparent 70%),
      radial-gradient(ellipse 380px 200px at 330px 720px, rgba(122,58,48,0.7), transparent 70%),
      radial-gradient(ellipse 260px 170px at 700px 680px, rgba(122,58,48,0.6), transparent 70%),
      linear-gradient(180deg, var(--sky) 0%, var(--sea) 30%, var(--deck) 48%, var(--wood) 66%, var(--cured) 82%, var(--mist) 100%);
  }
  .hero-photo::after {
    content: "";
    position: absolute; inset: 0;
    background: linear-gradient(180deg, rgba(255,255,255,0.4) 0%, rgba(255,255,255,0.05) 30%, rgba(255,255,255,0.05) 70%, rgba(255,255,255,0.6) 100%);
  }
  .band-edge { position: absolute; left: 0; width: 849px; }
  .band-edge--top { top: 0; height: 200px; }
  .band-edge--bottom { bottom: 0; height: 200px; }
  .band-edge path { fill: var(--orange); }

  .brand-panel {
    position: absolute;
    left: 48px; top: 30px;
    width: 452px; height: 207px;
    background: var(--white);
    border-radius: 14px;
    display: flex;
    align-items: center;
    justify-content: center;
  }
  .brand-name {
    color: var(--ink);
    font-size: 62px;
    line-height: 0.95;
    letter-spacing: 1px;
    text-align: center;
  }

  .activity-list {
    position: absolute;
    left: 0; top: 390px;
    width: 849px;
    list-style: none;
    text-align: center;
  }
  .activity {
    color: var(--orange);
    font-size: 58px;
    line-height: 80px;
    letter-spacing: 0.3px;
    text-shadow: 0 2px 3px var(--shadow), 0 0 14px rgba(45,25,8,0.45);
  }

  .contact {
    position: absolute;
    left: 0; top: 1050px;
    width: 849px;
    color: var(--white);
    text-align: center;
  }
  .contact__web {
    font-size: 48px;
    letter-spacing: 0.5px;
    line-height: 58px;
  }
  .contact__handle {
    margin-top: 4px;
    font-size: 60px;
    line-height: 66px;
    letter-spacing: 0.5px;
  }
</style>
</head>
<body>
<main class="poster">
  <div class="hero-photo" role="img" aria-label="Seaside table on a sailboat deck with a wine bottle, glass of red wine, sliced cured sausage, ham and olives on a wooden board"></div>

  <svg class="band-edge band-edge--top" viewBox="0 0 849 200" preserveAspectRatio="none" aria-hidden="true">
    <path d="M0 0 H849 V188 L830 183 L812 190 L790 180 L768 186 L745 178 L720 184 L700 175 L676 182 L650 176 L628 183 L604 177 L580 184 L556 178 L530 182 L505 174 L480 178 L455 171 L430 176 L400 170 L370 176 L340 169 L310 175 L280 168 L250 173 L220 167 L190 172 L160 166 L130 171 L100 165 L70 170 L40 164 L18 169 L0 165 Z"/>
  </svg>

  <svg class="band-edge band-edge--bottom" viewBox="0 0 849 200" preserveAspectRatio="none" aria-hidden="true">
    <path d="M0 200 H849 V20 L826 26 L804 18 L780 24 L756 16 L732 23 L708 17 L684 25 L660 19 L634 26 L610 18 L586 24 L560 17 L536 25 L510 19 L486 26 L460 18 L436 24 L410 17 L386 25 L360 19 L336 26 L310 18 L286 24 L260 17 L236 25 L210 19 L186 26 L160 18 L136 24 L110 17 L86 25 L60 19 L36 26 L14 19 L0 24 Z"/>
  </svg>

  <header class="brand-panel">
    <p class="brand-name">Coastal Table<br>Journeys Bay</p>
  </header>

  <ul class="activity-list">
    <li class="activity">Sangria Tasting</li>
    <li class="activity">Iberian Ham</li>
    <li class="activity">Charcuteries &amp; Sherry Wine Tasting</li>
    <li class="activity">Sailboat Experiences</li>
    <li class="activity">Picnic Experiences</li>
  </ul>

  <footer class="contact">
    <p class="contact__web">WWW.COASTALTABLEJOURNEYSBAY.EXAMPLE</p>
    <p class="contact__handle">@COASTALTABLEJOURNEYCTJ</p>
  </footer>
</main>
</body>
</html>
```